Delwyn's Pressure Washing Services

Starting a pressure washing business on my own in Central Valley California, not too much experience so affordable, I do houses, fences, driveways, cars, trailers, RVs. Planning to make this full-time hoping clientele picks up after having a nice business card. Design doesn't have to be flashy, more to the point, I like simplistic/personable. I do not want something exhausting to look at or with too much going on.

Target Market(s)

Residential, Commercial

Industry/Entity Type

Pressure Washing

Contact Information for Business Card

avalible Services

Font styles to use
Sans Serif

Colors
0054AA
0677BA
7BADD7
CADEEF
E8F1F8
0094D4
00A9DD
6FCCEA
C7EBF8
E9F6FB
00AB8E
00BBA5
67D7C9
C6EFE9
E9F9F6

```html
<!DOCTYPE html>
<html lang="en">
<head>
<meta charset="utf-8">
<title>Delwyn's Pressure Washing – Business Card</title>
<link rel="stylesheet" href="https://fonts.googleapis.com/css2?family=Audiowide&family=Montserrat:wght@400;500;700&display=swap">
<style>
  :root {
    --page: #e6e6e6;
    --card: #f4f8fc;
    --navy: #0b2466;
    --navy-deep: #001846;
    --royal: #0a3fa8;
    --brand: #4a8fd8;
    --sky: #6fccea;
    --sky-soft: #c7ebf8;
    --ice: #e9f6fb;
    --ink: #141414;
    --owner: #2f5fa8;
    --white: #ffffff;
  }
  * { box-sizing: border-box; margin: 0; padding: 0; }
  html, body { width: 685px; height: 1200px; overflow: hidden; background: var(--page); }
  body { position: relative; font-family: "Montserrat", sans-serif; }

  .card {
    position: absolute; left: 62px; width: 560px; height: 320px;
    background: var(--card); overflow: hidden;
    box-shadow: 0 3px 8px rgba(0,0,0,.22);
  }
  .card--front { top: 200px; }
  .card--back { top: 640px; }

  .wave-top {
    position: absolute; left: 0; top: 0; width: 100%; height: 110px;
    background: linear-gradient(170deg, var(--sky-soft) 0%, var(--ice) 45%, rgba(233,246,251,0) 80%);
  }
  .corner-sweep {
    position: absolute; left: 0; bottom: 0; width: 160px; height: 130px;
    background: linear-gradient(40deg, #5bb9e8 0%, #8fd0f0 45%, rgba(199,235,248,0) 75%);
    clip-path: ellipse(100% 100% at 0% 100%);
  }
  .bubbles {
    position: absolute; right: 0; bottom: 0; width: 110px; height: 120px;
    background: radial-gradient(circle at 60% 65%, #cfe9ee 0%, #b7dde6 30%, rgba(199,235,248,0) 70%);
  }
  .bubbles--small {
    left: 60px; top: 10px; right: auto; bottom: auto; width: 60px; height: 60px;
    background: radial-gradient(circle, #d6ecf1 0%, rgba(214,236,241,0) 70%);
  }

  .brand-name {
    font-family: "Audiowide", sans-serif; color: var(--brand); font-weight: 400;
    line-height: 1.05;
  }
  .card--front .brand-name {
    position: absolute; left: 0; width: 100%; top: 108px; text-align: center;
  }
  .card--front .brand-name .brand-line-1 { display: block; font-size: 38px; }
  .card--front .brand-name .brand-line-2 { display: block; font-size: 19px; margin-top: 6px; }

  .website-banner {
    position: absolute; left: 0; width: 100%; top: 270px; text-align: center;
    font-weight: 700; font-size: 15px; letter-spacing: 5px; color: var(--ink);
  }
  .website-banner .domain { color: var(--owner); }

  /* back */
  .services-panel { position: absolute; inset: 0; }
  .card--back .brand-name { position: absolute; left: 32px; top: 30px; }
  .card--back .brand-name .brand-line-1 { display: block; font-size: 24px; }
  .card--back .brand-name .brand-line-2 { display: block; font-size: 12px; margin-top: 3px; }

  .person { position: absolute; left: 32px; top: 114px; }
  .person-name { font-size: 20px; color: var(--ink); font-weight: 400; letter-spacing: .3px; }
  .person-name b { font-weight: 700; }
  .person-role { font-size: 13px; color: var(--owner); margin-top: 1px; }

  .contact-list { position: absolute; left: 0; top: 176px; list-style: none; }
  .contact-item { display: flex; align-items: center; height: 18px; margin-bottom: 13px; }
  .contact-tab {
    width: 51px; height: 18px; background: var(--navy);
    display: flex; justify-content: flex-end; align-items: center; padding-right: 6px;
  }
  .contact-text { margin-left: 11px; font-size: 15px; color: var(--ink); }

  .services-title {
    position: absolute; left: 384px; top: 80px;
    font-family: "Audiowide", sans-serif; font-size: 16px; color: var(--white);
  }
  .services-list { position: absolute; left: 396px; top: 110px; list-style: none; }
  .services-list li {
    font-family: "Audiowide", sans-serif; font-size: 12px; color: var(--white);
    height: 21px; display: flex; align-items: center;
  }
  .services-list li::before {
    content: ""; width: 6px; height: 6px; border-radius: 50%;
    background: var(--sky); margin-right: 13px;
  }
</style>
</head>
<body>

<section class="card card--front" aria-label="Card front">
  <div class="wave-top"></div>
  <div class="bubbles bubbles--small" role="img" aria-label="Soap bubbles"></div>
  <div class="corner-sweep"></div>
  <div class="bubbles" role="img" aria-label="Cluster of soap bubbles"></div>
  <h1 class="brand-name">
    <span class="brand-line-1">Delwyn's</span>
    <span class="brand-line-2">Pressure Washing</span>
  </h1>
  <p class="website-banner">www.<span class="domain">yourwebsite</span>.com</p>
</section>

<section class="card card--back" aria-label="Card back">
  <div class="wave-top"></div>
  <div class="corner-sweep" style="width:120px;height:60px;opacity:.6"></div>

  <svg class="services-panel" viewBox="0 0 560 320" width="560" height="320" aria-hidden="true">
    <defs>
      <linearGradient id="panelFill" x1="0" y1="0" x2="1" y2="1">
        <stop offset="0" stop-color="#001846"/>
        <stop offset=".55" stop-color="#0b2466"/>
        <stop offset="1" stop-color="#0a3fa8"/>
      </linearGradient>
    </defs>
    <polygon points="380,0 560,0 560,320 377,320 280,153" fill="url(#panelFill)"/>
    <path d="M380 82 Q373 82 373 92 L373 245 Q373 254 382 254 L493 254"
          fill="none" stroke="#ffffff" stroke-width="2"/>
    <rect x="491" y="250" width="14" height="8" rx="4" fill="#ffffff"/>
  </svg>

  <h2 class="brand-name">
    <span class="brand-line-1">Delwyn's</span>
    <span class="brand-line-2">Pressure Washing</span>
  </h2>

  <div class="person">
    <p class="person-name">DELWYN <b>MARSH</b></p>
    <p class="person-role">Owner</p>
  </div>

  <ul class="contact-list">
    <li class="contact-item">
      <span class="contact-tab">
        <svg width="12" height="12" viewBox="0 0 24 24" aria-hidden="true"><path d="M6.6 10.8a15 15 0 0 0 6.6 6.6l2.2-2.2a1 1 0 0 1 1-.25 11.4 11.4 0 0 0 3.6.57 1 1 0 0 1 1 1V20a1 1 0 0 1-1 1A17 17 0 0 1 3 4a1 1 0 0 1 1-1h3.5a1 1 0 0 1 1 1c0 1.25.2 2.45.57 3.57a1 1 0 0 1-.25 1z" fill="#fff"/></svg>
      </span>
      <span class="contact-text">2095550147</span>
    </li>
    <li class="contact-item">
      <span class="contact-tab">
        <svg width="12" height="10" viewBox="0 0 24 18" aria-hidden="true"><rect x="1" y="1" width="22" height="16" fill="none" stroke="#fff" stroke-width="2"/><path d="M1 1l11 9 11-9" fill="none" stroke="#fff" stroke-width="2"/></svg>
      </span>
      <span class="contact-text">info@yourmail.com</span>
    </li>
    <li class="contact-item">
      <span class="contact-tab">
        <svg width="12" height="12" viewBox="0 0 24 24" aria-hidden="true"><circle cx="12" cy="12" r="10" fill="none" stroke="#fff" stroke-width="2"/><path d="M2 12h20M12 2c3 3 3 17 0 20M12 2c-3 3-3 17 0 20" fill="none" stroke="#fff" stroke-width="1.6"/></svg>
      </span>
      <span class="contact-text">www.yourwebsite.com</span>
    </li>
  </ul>

  <h3 class="services-title">Our Services</h3>
  <ul class="services-list">
    <li>Houses</li>
    <li>Fences</li>
    <li>Driveways</li>
    <li>Cars</li>
    <li>Trailers</li>
    <li>RVs</li>
  </ul>
</section>

</body>
</html>
```